E-book cover required. Title is Nox, author Clara J Bennet. Would like large title at top and smaller name at bottom. Book is apocolyptic novel and design needs to reference blood. Simple would be best.

```html
<!DOCTYPE html>
<html lang="en">
<head>
<meta charset="utf-8">
<title>Nox — Clara J Bennet</title>
<link rel="stylesheet" href="https://fonts.googleapis.com/css2?family=Jost:wght@600;700&display=swap">
<style>
  :root {
    --ink: #0d0202;
    --night: #000000;
    --ember: #ff6a08;
    --blaze: #f0400a;
    --blood: #d01a06;
    --author-red: #e0230f;
    --author-orange: #ff6b12;
  }
  html, body {
    margin: 0;
    padding: 0;
    width: 750px;
    height: 1200px;
    overflow: hidden;
    background: var(--night);
  }
  .cover {
    display: block;
    width: 750px;
    height: 1200px;
    background: var(--night);
  }
  .cover__title {
    font-family: "Jost", "Futura", sans-serif;
    font-weight: 700;
    font-size: 352px;
    fill: var(--ink);
  }
  .cover__author {
    font-family: "Jost", "Futura", sans-serif;
    font-weight: 600;
    font-size: 82px;
  }
  .cover__author-first { fill: var(--author-red); }
  .cover__author-last { fill: var(--author-orange); }
  .stop-ember { stop-color: var(--ember); }
  .stop-blaze { stop-color: var(--blaze); }
  .stop-blood { stop-color: var(--blood); }
  .stop-night { stop-color: var(--night); }
</style>
</head>
<body>
  <svg class="cover" viewBox="0 0 750 1200" width="750" height="1200" xmlns="http://www.w3.org/2000/svg">
    <defs>
      <radialGradient id="glow-heat" cx="390" cy="250" r="430" gradientUnits="userSpaceOnUse" gradientTransform="translate(390 250) scale(1 0.95) translate(-390 -250)">
        <stop offset="0" class="stop-ember"/>
        <stop offset="0.45" class="stop-blaze"/>
        <stop offset="0.85" class="stop-blood"/>
        <stop offset="1" class="stop-blood"/>
      </radialGradient>
      <linearGradient id="glow-fade" x1="0" y1="0" x2="0" y2="1200" gradientUnits="userSpaceOnUse">
        <stop offset="0" class="stop-night" stop-opacity="0"/>
        <stop offset="0.3" class="stop-night" stop-opacity="0"/>
        <stop offset="0.4" class="stop-night" stop-opacity="0.55"/>
        <stop offset="0.48" class="stop-night" stop-opacity="1"/>
        <stop offset="1" class="stop-night" stop-opacity="1"/>
      </linearGradient>
      <filter id="glow-texture" x="0" y="0" width="100%" height="100%" color-interpolation-filters="sRGB">
        <feTurbulence type="fractalNoise" baseFrequency="0.055" numOctaves="2" seed="7" result="noise"/>
        <feDiffuseLighting in="noise" surfaceScale="2.2" diffuseConstant="1.05" lighting-color="#ffffff" result="bumps">
          <feDistantLight azimuth="225" elevation="55"/>
        </feDiffuseLighting>
        <feBlend in="SourceGraphic" in2="bumps" mode="multiply" result="textured"/>
        <feComposite in="textured" in2="SourceGraphic" operator="in"/>
      </filter>
    </defs>

    <g class="cover__glow" role="img" aria-label="Textured glowing blood-orange surface fading into black">
      <rect width="750" height="620" fill="url(#glow-heat)" filter="url(#glow-texture)"/>
      <rect width="750" height="1200" fill="url(#glow-fade)"/>
    </g>

    <text class="cover__title" x="388" y="345" text-anchor="middle" textLength="513" lengthAdjust="spacingAndGlyphs">NOX</text>

    <text class="cover__author" x="371" y="1128" text-anchor="middle" textLength="587" lengthAdjust="spacingAndGlyphs"><tspan class="cover__author-first">CLARA J </tspan><tspan class="cover__author-last">BENNET</tspan></text>
  </svg>
</body>
</html>
```